harborline slab pumping "just pump it"

I want very easy to understand cards that say everything we offer.
i want the company name/logo, phone number and email on the front of card.
i want the card to stand out, it can be red with black lettering.
on the back of the card i want it to list everything that we can do like a list
the motto is JUST PUMP IT.
the can be in the lower right corner of the back of the card

Target Market(s)

concrete contractors

Industry/Entity Type

Concrete

Contact Information for Business Card

back of the card
Owner:Marco Tellin
Phone:503)418-6093
Email: HSPumping@slabmail.example
address: 22816 se brindle ave Portland, OR 97236

Colors
ec1f27
000000
959595
5c5c5c
f04a50
ffffff
f37122

Requirements
Must have
• :we have years of experience in the world of concrete
• :our pumps can do up to 70 yards an hour
• :if you refer us to other contractors, will give you up to 10% off next pump job
• :don’t hesitate to call if you have any concrete related questions and to get a qoute
• Please put this on the front of the card, “just pump it” in the lower right corner

```html
<!DOCTYPE html>
<html lang="en">
<head>
<meta charset="utf-8">
<title>Harborline Slab Pumping – Business Card</title>
<link rel="stylesheet" href="https://fonts.googleapis.com/css2?family=Montserrat:wght@400;700&family=Roboto:wght@400;500&display=swap">
<style>
  :root {
    --red: #ec1f27;
    --black: #000000;
    --ink: #1c1c1c;
    --grey: #5c5c5c;
    --list-ink: #3b0c0e;
    --white: #ffffff;
    --backdrop: #e9e9e9;
  }
  * { box-sizing: border-box; margin: 0; padding: 0; }
  html, body {
    width: 1125px; height: 1200px; overflow: hidden;
    background: var(--backdrop);
  }
  .canvas { position: relative; width: 1125px; height: 1200px; }

  .card {
    position: absolute; left: 162px; width: 800px; height: 457px;
    box-shadow: 0 2px 10px rgba(0,0,0,.18);
  }
  .card--front { top: 95px; background: var(--white); overflow: hidden; }
  .card--back { top: 611px; background: var(--red); }

  .front__stripe {
    position: absolute; left: 0; top: 0; width: 66px; height: 100%;
    background: var(--red);
  }
  .brand {
    position: absolute; left: 27px; top: 55px;
    display: flex; align-items: center; gap: 14px;
  }
  .brand__dot {
    width: 82px; height: 82px; border-radius: 50%;
    background: var(--red); border: 3px solid var(--white);
  }
  .brand__name {
    font-family: "Montserrat", sans-serif; font-weight: 700;
    font-size: 30px; letter-spacing: 1px; color: var(--red);
    text-transform: uppercase;
  }

  .contact {
    position: absolute; right: 40px; top: 258px;
    text-align: right; font-family: "Montserrat", sans-serif;
  }
  .contact__name {
    font-weight: 700; font-size: 28px; letter-spacing: 1px;
    color: var(--red); text-transform: uppercase; margin-bottom: 14px;
  }
  .contact__line {
    display: flex; justify-content: flex-end; align-items: center; gap: 9px;
    font-size: 18px; color: var(--grey); line-height: 25px;
  }
  .contact__line svg { width: 18px; height: 18px; fill: var(--grey); }
  .tagline {
    position: absolute; right: 40px; top: 396px;
    font-family: "Montserrat", sans-serif; font-size: 19px; color: var(--ink);
  }

  .back__mark { position: absolute; left: 162px; top: 138px; width: 196px; text-align: center; }
  .back__circle { width: 196px; height: 196px; border-radius: 50%; background: var(--black); }
  .back__name {
    margin-top: 12px; font-family: "Montserrat", sans-serif; font-weight: 700;
    font-size: 13px; letter-spacing: 1px; color: var(--black); text-transform: uppercase;
    white-space: nowrap; margin-left: -40px; margin-right: -40px;
  }
  .back__divider {
    position: absolute; left: 406px; top: 136px; width: 1px; height: 201px;
    background: var(--list-ink);
  }
  .services {
    position: absolute; left: 450px; top: 137px;
    font-family: "Roboto", sans-serif; font-size: 20px; line-height: 25px;
    color: var(--list-ink); list-style: none;
  }
  .services li::before { content: "•"; display: inline-block; width: 20px; }
  .motto {
    position: absolute; right: 24px; bottom: 18px;
    font-family: "Roboto", sans-serif; font-weight: 500; font-size: 19px;
    color: var(--list-ink);
  }
</style>
</head>
<body>
<main class="canvas">
  <section class="card card--front">
    <div class="front__stripe"></div>
    <div class="brand">
      <div class="brand__dot"></div>
      <span class="brand__name">Harborline Slab Pumping</span>
    </div>
    <div class="contact">
      <p class="contact__name">Marco Tellin</p>
      <p class="contact__line">503)418-6093
        <svg viewBox="0 0 24 24" aria-hidden="true"><path d="M6.6 10.8a15.1 15.1 0 0 0 6.6 6.6l2.2-2.2a1 1 0 0 1 1-.25 11.4 11.4 0 0 0 3.6.57 1 1 0 0 1 1 1V20a1 1 0 0 1-1 1A17 17 0 0 1 3 4a1 1 0 0 1 1-1h3.5a1 1 0 0 1 1 1c0 1.25.2 2.45.57 3.57a1 1 0 0 1-.25 1z"/></svg>
      </p>
      <p class="contact__line">HSPumping@slabmail.example
        <svg viewBox="0 0 24 24" aria-hidden="true"><path d="M2 5h20v14H2zm2 2v.5l8 5 8-5V7zm0 2.8V17h16V9.8l-8 5z"/></svg>
      </p>
      <p class="contact__line">www.HSPumping.example
        <svg viewBox="0 0 24 24" aria-hidden="true"><path d="M12 2a10 10 0 1 0 0 20 10 10 0 0 0 0-20zm-1 17.9A8 8 0 0 1 4.1 10.9L9 15.8v1.1a2 2 0 0 0 2 2zm6.9-2.5a2 2 0 0 0-1.9-1.4h-1v-3a1 1 0 0 0-1-1H8v-2h2a1 1 0 0 0 1-1V7h2a2 2 0 0 0 2-2v-.4a8 8 0 0 1 2.9 12.8z"/></svg>
      </p>
    </div>
    <p class="tagline">Our pumps can do up to 70 yards an hour</p>
  </section>

  <section class="card card--back">
    <div class="back__mark">
      <div class="back__circle"></div>
      <p class="back__name">Harborline Slab Pumping</p>
    </div>
    <div class="back__divider"></div>
    <ul class="services">
      <li>Consectetur</li>
      <li>Potestate</li>
      <li>Desperationem</li>
      <li>Epicureum</li>
      <li>Varietates</li>
      <li>Admirabilia</li>
      <li>Democriteum</li>
      <li>Iucundius</li>
    </ul>
    <p class="motto">motto is JUST PUMP IT</p>
  </section>
</main>
</body>
</html>
```